Criação de Cartao de Visita para Vigor & Equilíbrio
" Venda de Suplementos Alimentares/Nutricionais, principalmente via whatsapp e facebook, fazemos entregas e aceitamos cartões. Ainda não possuimos loja física. Cobrimos qualquer oferta de site ou loja nacional. "

```html
<!DOCTYPE html>
<html lang="pt-BR">
<head>
<meta charset="utf-8">
<title>Vigor &amp; Equilíbrio — Cartão de Visita</title>
<link rel="stylesheet" href="https://fonts.googleapis.com/css2?family=Exo+2:wght@500;700;800&display=swap">
<style>
  :root {
    --page: #e9e6e1;
    --paper: #ffffff;
    --ink: #1b1b1b;
    --ink-soft: #4a4a4a;
    --gold: #f2b705;
    --gold-deep: #d89a00;
    --steel-dark: #161616;
    --steel-mid: #2c2c2c;
  }
  * { box-sizing: border-box; margin: 0; padding: 0; }
  html, body {
    width: 1200px; height: 1200px; overflow: hidden;
    background: var(--page);
    font-family: "Exo 2", Arial, sans-serif;
  }
  .sheet {
    width: 1200px; height: 1200px;
    display: flex; flex-direction: column; align-items: center; justify-content: center;
    gap: 60px;
  }
  .card {
    position: relative; width: 900px; height: 514px; overflow: hidden;
    box-shadow: 0 10px 30px rgba(0,0,0,.18);
  }

  /* front */
  .card--front { background: var(--paper); }
  .brand {
    position: absolute; display: flex; align-items: center; gap: 18px;
  }
  .brand__dot { width: 46px; height: 46px; border-radius: 50%; background: var(--gold); flex: none; }
  .brand__name { font-weight: 800; letter-spacing: .5px; white-space: nowrap; }
  .card--front .brand { left: 60px; top: 210px; }
  .card--front .brand__name { font-size: 40px; color: var(--ink); }

  .contact {
    position: absolute; right: 56px; top: 150px; text-align: right; color: var(--ink);
  }
  .contact__name { font-size: 26px; font-weight: 800; letter-spacing: .5px; }
  .contact__role { font-size: 17px; font-weight: 500; color: var(--ink-soft); margin-bottom: 22px; }
  .contact__list { list-style: none; }
  .contact__item {
    display: flex; align-items: center; justify-content: flex-end; gap: 12px;
    font-size: 18px; font-weight: 700; line-height: 1.15; margin-bottom: 10px;
  }
  .contact__icon {
    width: 24px; height: 24px; background: var(--gold); border-radius: 3px;
    display: flex; align-items: center; justify-content: center; flex: none;
  }
  .contact__icon svg { width: 15px; height: 15px; }
  .front-band { position: absolute; left: 0; bottom: 0; width: 900px; height: 90px; }

  /* back */
  .card--back { background: var(--steel-dark); }
  .steel-plate {
    position: absolute; inset: 0;
    background: radial-gradient(circle at 35% 40%, var(--steel-mid), var(--steel-dark) 75%);
  }
  .gold-glow {
    position: absolute; right: 0; top: 0; width: 360px; height: 514px;
    background: linear-gradient(100deg, rgba(242,183,5,0) 0%, rgba(242,183,5,.55) 55%, rgba(216,154,0,.8) 100%);
  }
  .card--back .brand { left: 90px; top: 225px; }
  .card--back .brand__name { font-size: 46px; color: var(--gold); }
</style>
</head>
<body>
<main class="sheet">

  <section class="card card--front" aria-label="Frente do cartão">
    <div class="brand">
      <span class="brand__dot"></span>
      <span class="brand__name">Vigor &amp; Equilíbrio</span>
    </div>

    <div class="contact">
      <p class="contact__name">NOME SOBRENOME</p>
      <p class="contact__role">Função</p>
      <ul class="contact__list">
        <li class="contact__item">contato@vigorequilibrio.com.br
          <span class="contact__icon"><svg viewBox="0 0 16 16"><rect x="2" y="4" width="12" height="8" fill="none" stroke="#1b1b1b" stroke-width="1.6"/><path d="M2 4l6 5 6-5" fill="none" stroke="#1b1b1b" stroke-width="1.6"/></svg></span></li>
        <li class="contact__item">www.vigorequilibrio.com.br
          <span class="contact__icon"><svg viewBox="0 0 16 16"><circle cx="8" cy="8" r="6" fill="none" stroke="#1b1b1b" stroke-width="1.6"/><path d="M2 8h12M8 2c3 3 3 9 0 12M8 2c-3 3-3 9 0 12" fill="none" stroke="#1b1b1b" stroke-width="1.2"/></svg></span></li>
        <li class="contact__item">(11) 99999-9999
          <span class="contact__icon"><svg viewBox="0 0 16 16"><rect x="4.5" y="1.5" width="7" height="13" rx="1.5" fill="none" stroke="#1b1b1b" stroke-width="1.6"/><circle cx="8" cy="12" r=".9" fill="#1b1b1b"/></svg></span></li>
        <li class="contact__item">(11) 99999-9999
          <span class="contact__icon"><svg viewBox="0 0 16 16"><path d="M3 2h3l1.5 3.5-2 1.3a8 8 0 0 0 3.7 3.7l1.3-2L14 10v3a1 1 0 0 1-1 1A11 11 0 0 1 2 3a1 1 0 0 1 1-1z" fill="#1b1b1b"/></svg></span></li>
        <li class="contact__item">Endereço Completo, 000 Bairro<br>Cidade/Estado
          <span class="contact__icon"><svg viewBox="0 0 16 16"><path d="M8 15s5-5.2 5-8.5A5 5 0 0 0 3 6.5C3 9.8 8 15 8 15z" fill="#1b1b1b"/><circle cx="8" cy="6.5" r="1.8" fill="#f2b705"/></svg></span></li>
      </ul>
    </div>

    <svg class="front-band" viewBox="0 0 900 90" preserveAspectRatio="none" aria-hidden="true">
      <path d="M0 40 C250 70 600 80 900 78 L900 90 L0 90 Z" fill="var(--gold)"/>
      <path d="M0 62 C250 84 600 88 900 86 L900 90 L0 90 Z" fill="var(--ink)"/>
    </svg>
  </section>

  <section class="card card--back" aria-label="Verso do cartão">
    <div class="steel-plate" role="img" aria-label="Textura de chapa de aço xadrez escura"></div>
    <div class="gold-glow" role="img" aria-label="Área decorativa dourada ampliada da marca"></div>
    <div class="brand">
      <span class="brand__dot"></span>
      <span class="brand__name">Vigor &amp; Equilíbrio</span>
    </div>
  </section>

</main>
</body>
</html>
```